SINGLE PAGE WEBSITE needed for Haunted-House Style Horror Event!

PROJECT:
Single page website to advertise "Bolting Shadows"

ABOUT BOLTING SHADOWS:
Bolting Shadows is a Horror Experience event, that will be held on June 1st 2019 at The Ember Playhouse in Sydney.

At the event, patrons will enter 6 different rooms and have a horror experience in each one.

There's a bar on-site for them to drink as well.

NEEDS FOR THE WEBSITE:
1. Video banner at top, and scrolling photos after video finishes, and text over the top of the video with the name and date of the event
eg.
"A Night of Immersive Horror Experiences"
"The Ember Playhouse | June 1st, 2019"

2. Multiple Book Now buttons on the page, which will link to an external booking platform

3. It should say somewhere "Produced by [MARBLE LANTERN PRODUCTIONS LOGO]"

4. A "Next Steps" section that has the steps for them to complete, such as
- Purchase your ticket HERE for one of our waves
- Rock up at the Ember Playhouse on June 1st at your wave time
- Experience each of our 6 Interactive Horror Rooms
- Grab some drinks at the bar, a bite to eat, and enjoy a fantastic night out!

Other things that should be included somewhere:
- Testimonials
- FAQs (maybe as a dropdown, so it doesn't take up much space?)
- Contact Form on Footer

- - - -

Images, logos, and more attached!

Industry/Entity Type

Events

Coding

Coded - Design and coding required

Number of Pages Required

1 page

Requirements
Nice to have
• 1. Video banner at top, and scrolling photos after video finishes, and text over the top of the video with the name and date of the event
• eg.
• "A Night of Immersive Horror Experiences"
• "The Ember Playhouse | June 1st, 2019"
• 2. multiple Book Now buttons on the page, which will link to an external booking platform
• 3. It should say somewhere "Produced by [Marble Lantern Productions LOGO]" with the Marble Lantern logo
• 4. A "Next Steps" section that has the steps for them to complete, such as
• - Purchase your ticket HERE for one of our waves
• - Rock up at the Ember Playhouse on June 1st at your wave time
• - Experience each of our 6 Interactive Horror Rooms
• - Grab some drinks at the bar, a bite to eat, and enjoy a fantastic night out!
• Other things that should be included somewhere:
• - Testimonials
• - FAQs (maybe as a dropdown, so it doesn't take up much space?)
• - Contact Form on Footer

```html
<!DOCTYPE html>
<html lang="en">
<head>
<meta charset="utf-8">
<title>Bolting Shadows – Interactive Horror Experience</title>
<link rel="stylesheet" href="https://fonts.googleapis.com/css2?family=Luckiest+Guy&family=Roboto:ital,wght@0,400;0,500;0,700;1,700&display=swap">
<style>
:root{
  --lime:#8cc63e;
  --lime-deep:#6e9f22;
  --lime-dark:#4f7a12;
  --ink:#0a0a0a;
  --night:#141414;
  --white:#ffffff;
  --muted:#d7e6bf;
  --display:"Luckiest Guy", "Impact", sans-serif;
  --text:"Roboto", "Arial", sans-serif;
}
*{margin:0;padding:0;box-sizing:border-box}
html,body{width:1200px;height:3854px;overflow:hidden;background:var(--ink)}
body{position:relative;font-family:var(--text);color:var(--white)}
section,header,footer{position:absolute;left:0;width:1200px;overflow:hidden}
.h-title{font-family:var(--display);text-align:center;font-size:34px;letter-spacing:1px;color:var(--white);position:absolute;left:0;width:100%}
.h-sub{position:absolute;left:0;width:100%;text-align:center;font-weight:700;font-size:14px;line-height:20px}
.title-mark{position:absolute;left:50%;width:22px;height:34px;margin-left:-11px;background:var(--white);border-radius:8px 8px 2px 2px;opacity:.92}
.btn-book{display:flex;align-items:center;justify-content:center;font-family:var(--display);letter-spacing:1px;border-radius:40px}

/* hero */
.hero{top:0;height:601px;background:
  radial-gradient(ellipse 420px 160px at 600px 210px, rgba(140,198,62,.35), transparent 70%),
  radial-gradient(ellipse 300px 220px at 1000px 170px, rgba(120,170,40,.35), transparent 70%),
  linear-gradient(180deg,#0d1208 0%,#060805 70%,#000 100%)}
.brand{position:absolute;left:96px;top:14px;font-family:var(--text);font-weight:700;font-size:22px;line-height:24px;color:var(--lime);width:180px}
.nav{position:absolute;right:100px;top:22px;display:flex;align-items:center;gap:0}
.nav a{font-family:var(--display);font-size:15px;color:var(--white);text-decoration:none;margin-left:30px;letter-spacing:.5px}
.nav a.is-active{color:var(--lime)}
.nav .btn-book{background:var(--lime);color:var(--white);width:114px;height:40px;margin-left:30px;font-size:15px}
.hero-name{position:absolute;left:300px;top:135px;width:600px;height:140px;display:flex;align-items:center;justify-content:center;gap:18px;background:var(--lime);border-radius:6px}
.hero-name span{font-family:var(--text);font-weight:700;font-size:60px;color:var(--ink)}
.hero-name i{display:block;width:30px;height:30px;background:var(--ink)}
.tagline{position:absolute;top:342px;left:0;width:100%;text-align:center;font-family:var(--text);font-style:italic;font-weight:700;font-size:31px;letter-spacing:5px;text-transform:uppercase}
.venue{position:absolute;top:408px;left:0;width:100%;text-align:center;font-size:23px;color:#cfcfcf;letter-spacing:1px}
.url{position:absolute;top:454px;left:0;width:100%;text-align:center;font-size:22px;color:#bdbdbd;letter-spacing:2px}
.dots{position:absolute;top:518px;left:532px;display:flex;gap:7px}
.dots b{display:block;width:26px;height:7px;border-radius:4px;background:#3a3a3a}
.dots b.on{background:var(--lime)}

/* ticket band */
.ticket{top:601px;height:175px;background:linear-gradient(90deg,var(--lime-deep) 0%,var(--lime) 60%,var(--lime-deep) 100%)}
.ticket-photo{position:absolute;left:560px;top:0;width:330px;height:175px;background:linear-gradient(90deg,rgba(140,198,62,0),rgba(170,200,120,.55) 50%,rgba(140,198,62,0))}
.ticket h2{position:absolute;left:90px;top:662px;top:61px;font-family:var(--display);font-size:22px;line-height:28px;letter-spacing:1px;width:520px;font-weight:400}
.ticket .btn-book{position:absolute;left:894px;top:59px;width:204px;height:58px;background:var(--ink);color:var(--white);font-size:21px}

/* about */
.about{top:776px;height:758px;background:linear-gradient(180deg,#1b1b1b 0%,#111 60%,#1a1a1a 100%)}
.about .title-mark{top:85px}
.about .h-title{top:128px}
.about .h-sub{top:180px}
.about-copy{position:absolute;left:90px;top:222px;width:485px;font-size:14px;line-height:21px}
.about-copy p{margin-bottom:20px}
.video{position:absolute;left:610px;top:224px;width:490px;height:365px;background:linear-gradient(135deg,#3b4a60 0%,#5a5f6b 45%,#2a2f3d 100%)}
.play{position:absolute;left:205px;top:144px}
.producer{position:absolute;left:90px;top:604px;display:flex;align-items:center;gap:10px}
.producer i{display:block;width:42px;height:42px;background:#d0d0d0}
.producer span{font-family:var(--text);font-weight:700;font-size:15px;line-height:19px;color:#d0d0d0;width:170px}

/* testimonials */
.testimonials{top:1534px;height:669px;background:radial-gradient(ellipse 500px 330px at 600px 300px,#97ca4f,var(--lime-deep) 80%)}
.testimonials .title-mark{top:88px}
.testimonials .h-title{top:130px}
.testimonials .h-sub{top:176px}
.avatar{position:absolute;left:567px;top:258px;width:66px;height:66px;border-radius:50%;background:#f2f2f2;border:3px solid #fff}
.quote{position:absolute;left:0;top:330px;width:100%;text-align:center;font-family:var(--display);font-size:44px;color:var(--white)}
.quote-text{position:absolute;left:245px;top:380px;width:710px;text-align:center;font-size:14px;line-height:21px;color:var(--muted)}
.quote-name{position:absolute;left:0;top:546px;width:100%;text-align:center;font-weight:700;font-style:italic;font-size:15px;color:var(--ink)}

/* faqs */
.faqs{top:2203px;height:822px;background:linear-gradient(180deg,#121212,#050505 70%,#0d0d0d)}
.faqs .title-mark{top:92px}
.faqs .h-title{top:134px}
.faqs .h-sub{top:184px}
.faq-list{position:absolute;left:167px;top:264px;width:863px}
.faq{border:1.5px solid #d9d9d9;border-radius:3px;margin-bottom:20px}
.faq-q{display:flex;align-items:center;height:36px;padding-left:14px;font-weight:700;font-size:14px}
.faq-q svg{margin-right:14px}
.faq.open .faq-q{color:var(--lime)}
.faq.open{height:273px}
.faq-a{padding:4px 30px 0 52px;font-size:13px;line-height:20px;color:#e6e6e6}
.faq-a p{margin-bottom:20px}

/* contact */
.contact{top:3025px;height:758px;background:radial-gradient(ellipse 700px 400px at 600px 300px,#9acd52,var(--lime-deep) 85%)}
.contact .title-mark{top:90px}
.contact .h-title{top:132px}
.contact .h-sub{top:184px;font-weight:500}
.form{position:absolute;left:90px;top:244px;width:491px}
.field{height:40px;border:1.5px solid #e8f3d8;margin-bottom:18px;padding:0 14px;display:flex;align-items:center;font-size:13px;font-weight:500;color:var(--white)}
.field.message{height:136px;align-items:flex-start;padding-top:12px}
.send{height:40px;background:var(--white);color:var(--ink);font-weight:700;font-size:14px;display:flex;align-items:center;justify-content:center;letter-spacing:.5px}
.map{position:absolute;left:609px;top:244px;width:491px;height:283px;background:linear-gradient(135deg,#aad3df 0%,#cfe6c8 40%,#e8e4d8 70%,#aad3df 100%)}
.info{position:absolute;left:609px;top:546px;font-size:14px;font-weight:700;line-height:18px}
.info-row{display:flex;align-items:flex-start;gap:14px;margin-bottom:14px}
.info-row svg{flex:none;margin-top:1px}

/* footer */
.site-footer{top:3783px;height:71px;background:var(--ink)}
.copy{position:absolute;left:90px;top:27px;font-size:13px;font-weight:500}
.social{position:absolute;right:100px;top:22px;display:flex;gap:8px}
.social i{display:block;width:26px;height:26px;border-radius:50%;background:var(--white)}
</style>
</head>
<body>

<header class="hero">
  <div class="brand">BOLTING SHADOWS</div>
  <nav class="nav">
    <a href="#" class="is-active">HOME</a>
    <a href="#testimonials">TESTIMONIALS</a>
    <a href="#faqs">FAQS</a>
    <a href="#contact">CONTACT US</a>
    <a href="#" class="btn-book">BOOK NOW</a>
  </nav>
  <div class="hero-name"><i></i><span>BOLTING SHADOWS</span></div>
  <div class="tagline">Interactive Horror Experience</div>
  <div class="venue">The Ember Playhouse | June 1st, 2019</div>
  <div class="url">www.boltingshadows.com.au</div>
  <div class="dots"><b class="on"></b><b></b><b></b><b></b></div>
</header>

<section class="ticket">
  <div class="ticket-photo" role="img" aria-label="Photo of a costumed horror performer fading into the green band"></div>
  <h2>PURCHASE YOUR TICKET HERE FOR &nbsp;ONE OF OUR WAVES</h2>
  <a class="btn-book" href="#">BOOK NOW</a>
</section>

<section class="about">
  <div class="title-mark" role="img" aria-label="Small zombie hand illustration"></div>
  <h2 class="h-title">WHAT'S "BOLTING SHADOWS"</h2>
  <p class="h-sub">Grab some drinks at the bar, a bite to eat, and enjoy a fantastic night out!</p>
  <div class="about-copy">
    <p>Lorem Ipsum is simply dummy text of the printing and typesetting industry. Lorem Ipsum has been the industry's standard dummy text ever since the 1500s, when an unknown printer took a galley of type and scrambled it to make a type specimen book. It has survived not only five centuries, but also the leap into electronic typesetting, remaining essentially unchanged.</p>
    <p>Lorem Ipsum is simply dummy text of the printing and typesetting industry. Lorem Ipsum has been the industry's standard dummy text ever since the 1500s.</p>
    <p>Lorem Ipsum is simply dummy text of the printing and typesetting industry. Lorem Ipsum has been the industry's standard dummy text ever since the 1500s, when an unknown printer took a galley of type and scrambled it to make a type specimen book. It has survived not only five centuries, but also the leap into electronic typesetting, remaining essentially unchanged.</p>
  </div>
  <div class="video" role="img" aria-label="Video still of two costumed horror performers in a dim room">
    <svg class="play" width="80" height="80" viewBox="0 0 80 80"><circle cx="40" cy="40" r="38" fill="#8cc63e"/><path d="M31 24 L58 40 L31 56 Z" fill="#1a1a1a"/></svg>
  </div>
  <div class="producer"><i></i><span>MARBLE LANTERN PRODUCTIONS</span></div>
</section>

<section class="testimonials" id="testimonials">
  <div class="title-mark" role="img" aria-label="Small zombie hand illustration"></div>
  <h2 class="h-title">TESTIMONIALS</h2>
  <p class="h-sub">Lorem Ipsum is simply dummy text of the printing and typesetting industry. Lorem Ipsum has been the<br>industry's standard dummy text ever since the 1500s</p>
  <div class="avatar" role="img" aria-label="Reviewer portrait"></div>
  <div class="quote">&ldquo;</div>
  <p class="quote-text">Lorem Ipsum is simply dummy text of the printing and typesetting industry. Lorem Ipsum has been the industry's standard dummy text ever since the 1500s, when an unknown printer took a galley of type and scrambled it to make a type specimen book. It has survived not only five centuries, but also the leap into electronic typesetting, remaining essentially unchanged. It was popularised in the 1960s with the release of Letraset sheets containing Lorem Ipsum passages, and more recently with desktop publishing software like Aldus PageMaker including versions of Lorem Ipsum.</p>
  <p class="quote-name">Martin Hale</p>
</section>

<section class="faqs" id="faqs">
  <div class="title-mark" role="img" aria-label="Small zombie hand illustration"></div>
  <h2 class="h-title">FAQS</h2>
  <p class="h-sub">Lorem Ipsum is simply dummy text of the printing and typesetting industry. Lorem Ipsum has been the<br>industry's standard dummy text ever since the 1500s</p>
  <div class="faq-list">
    <div class="faq open">
      <div class="faq-q"><svg width="12" height="8" viewBox="0 0 12 8"><path d="M1 1 L6 6 L11 1" stroke="#fff" stroke-width="2" fill="none"/></svg>This looks scary, is this a haunted house?</div>
      <div class="faq-a">
        <p>Lorem Ipsum is simply dummy text of the printing and typesetting industry. Lorem Ipsum has been the industry's standard dummy text ever since the 1500s, when an unknown printer took a galley of type and scrambled it to make a type specimen book. It has survived not only five centuries, but also the leap into electronic typesetting, remaining essentially unchanged. It was popularised in the 1960s with the release of Letraset sheets containing Lorem Ipsum passages, and more recently with desktop publishing software like Aldus PageMaker including versions of Lorem Ipsum.</p>
        <p>Lorem Ipsum is simply dummy text of the printing and typesetting industry. Lorem Ipsum has been the industry's standard dummy text ever since the 1500s</p>
      </div>
    </div>
    <div class="faq"><div class="faq-q"><svg width="8" height="12" viewBox="0 0 8 12"><path d="M1 1 L6 6 L1 11" stroke="#fff" stroke-width="2" fill="none"/></svg>What is Lorem Ipsum?</div></div>
    <div class="faq"><div class="faq-q"><svg width="8" height="12" viewBox="0 0 8 12"><path d="M1 1 L6 6 L1 11" stroke="#fff" stroke-width="2" fill="none"/></svg>What is Lorem Ipsum?</div></div>
    <div class="faq"><div class="faq-q"><svg width="8" height="12" viewBox="0 0 8 12"><path d="M1 1 L6 6 L1 11" stroke="#fff" stroke-width="2" fill="none"/></svg>What is Lorem Ipsum?</div></div>
  </div>
</section>

<section class="contact" id="contact">
  <div class="title-mark" role="img" aria-label="Small zombie hand illustration"></div>
  <h2 class="h-title">CONTACT US</h2>
  <p class="h-sub">Hello, &nbsp;So you want to contact us? &nbsp;That's a lot easier than our Escapes, just drop us a message here!</p>
  <div class="form">
    <div class="field">NAME</div>
    <div class="field">E-MAIL ADDRESS</div>
    <div class="field">PHONE NO</div>
    <div class="field">SUBJECT</div>
    <div class="field message">MESSAGE</div>
    <div class="send">SEND YOUR MESSAGE</div>
  </div>
  <div class="map" role="img" aria-label="Street map showing the venue location by the harbour"></div>
  <div class="info">
    <div class="info-row"><svg width="14" height="14" viewBox="0 0 14 14"><rect x="1" y="1" width="12" height="12" fill="#fff"/></svg><span>BOLTING SHADOWS<br>28 Cinder Lane, Marrickville NSW 2204</span></div>
    <div class="info-row"><svg width="14" height="14" viewBox="0 0 14 14"><path d="M3 1 L5.5 1 L6.5 4 L5 5.5 Q6.5 8.5 8.5 9 L10 7.5 L13 8.5 L13 11 Q12 13 10 13 Q2 11 1 3 Q1 1 3 1 Z" fill="#fff"/></svg><span>02-5550-0147</span></div>
    <div class="info-row"><svg width="14" height="14" viewBox="0 0 14 14"><rect x="1" y="3" width="12" height="9" fill="#fff"/><path d="M1 3 L7 8 L13 3" stroke="#6e9f22" stroke-width="1.2" fill="none"/></svg><span>hello@boltingshadows.com.au</span></div>
  </div>
</section>

<footer class="site-footer">
  <p class="copy">&copy; Copyright 2019 BOLTING SHADOWS. All rights reserved</p>
  <div class="social"><i></i><i></i><i></i></div>
</footer>

</body>
</html>
```